Hautglanz Kosmetik Göttingen sucht Werbeplakat für Außenwerbung
Zielgruppe
Wir sind ein junges modernes Kosmetikstudio im Herzen der Studentenstadt Göttingen.
Wir bieten allen Zielgruppen ein attraktives Preisleistungsverhältnis.
http://www.hautglanz-kosmetik.example/
Aufgabenstellung
Wir benötigen für ein großes Außenplakat eine ansprechende Werbung für unser Studio.
Schwerpunkt sollte dabei unser Angebot für dauerhafte Haarentfernung mittels IPL Technologie sein.
Es soll optisch ansprechend sein (eye catcher) und auch Studenten ansprechen.

```html
<!DOCTYPE html>
<html lang="de">
<head>
<meta charset="utf-8">
<title>Hautglanz Kosmetik – Plakatvarianten</title>
<link href="https://fonts.googleapis.com/css2?family=Signika:wght@300;400;600;700&display=swap" rel="stylesheet">
<style>
  :root {
    --paper: #ffffff;
    --frame: #9a9a9a;
    --grey-text: #6b6b6b;
    --body-text: #4a4a4a;
    --brand-purple: #5b3a9a;
    --brown-dark: #5a2a14;
    --brown-band-top: #a5705a;
    --brown-band-mid: #6e3420;
    --brown-band-bottom: #b07a63;
    --blue-dark: #1a66b5;
    --blue-band-mid: #1f6fc0;
    --blue-band-bottom: #7ab8ec;
    --skin-light: #e8b6a0;
    --skin-mid: #d49a82;
    --skin-dark: #b87a64;
  }
  * { box-sizing: border-box; margin: 0; padding: 0; }
  html, body { width: 1200px; height: 843px; overflow: hidden; background: var(--paper); }
  body { position: relative; font-family: "Signika", sans-serif; }

  .poster {
    position: absolute; top: 51px; width: 525px; height: 742px;
    border: 1px solid var(--frame); background: var(--paper); overflow: hidden;
  }
  .poster--brown { left: 51px; --accent: var(--brown-dark); --band-a: var(--brown-band-top); --band-b: var(--brown-band-mid); --band-c: var(--brown-band-bottom); }
  .poster--blue { left: 625px; --accent: var(--blue-dark); --band-a: var(--blue-band-mid); --band-b: var(--blue-band-mid); --band-c: var(--blue-band-bottom); }

  .brand-name {
    position: absolute; top: 38px; left: 0; width: 100%; text-align: center;
    font-weight: 700; font-size: 58px; line-height: 70px; color: var(--brand-purple);
  }
  .tagline {
    position: absolute; top: 120px; left: 0; width: 100%; text-align: center;
    font-weight: 600; font-size: 24px; line-height: 30px; color: var(--grey-text);
  }
  .band {
    position: absolute; left: 0; width: 100%; height: 36px;
    display: flex; align-items: center; padding-left: 22px;
    white-space: nowrap; overflow: hidden;
    background: linear-gradient(to bottom, var(--band-a), var(--band-b) 45%, var(--band-b) 60%, var(--band-c));
    color: #fff;
  }
  .band span { flex: none; line-height: 26px; border-left: 1px solid rgba(255,255,255,0.35); }
  .band span:first-child { padding-left: 0; border-left: none; }
  .services { top: 162px; font-size: 14px; font-weight: 400; }
  .services span { padding: 0 8px; }
  .contact { top: 651px; font-size: 11.5px; font-weight: 300; }
  .contact span { padding: 0 7px; }

  .photo { position: absolute; left: 0; top: 197px; width: 100%; }
  .photo--torn { height: 243px; }
  .photo--plain {
    height: 226px;
    background: radial-gradient(ellipse at 50% 60%, var(--skin-light), var(--skin-mid) 60%, var(--skin-dark));
  }

  .headline {
    position: absolute; left: 0; width: 100%; text-align: center;
    font-weight: 700; font-size: 36px; line-height: 42px; color: var(--accent);
  }
  .subline {
    position: absolute; left: 0; width: 100%; text-align: center;
    font-weight: 300; font-size: 26px; line-height: 30px; color: var(--accent);
  }
  .poster--brown .headline { top: 474px; }
  .poster--brown .subline { top: 517px; }
  .poster--blue .headline { top: 447px; }
  .poster--blue .subline { top: 490px; }

  .benefits {
    position: absolute; left: 58px; list-style: none;
    font-weight: 600; font-size: 16px; line-height: 20px; color: var(--body-text);
  }
  .poster--brown .benefits { top: 558px; }
  .poster--blue .benefits { top: 531px; }
  .benefits li { position: relative; padding-left: 14px; }
  .benefits li::before {
    content: ""; position: absolute; left: 0; top: 7px; width: 7px; height: 7px;
    border-radius: 50%; background: var(--accent);
  }

  .hours {
    position: absolute; top: 696px; left: 24px; right: 16px;
    display: flex; gap: 16px; font-size: 10.5px; line-height: 14px; color: var(--body-text); font-weight: 300;
    white-space: nowrap;
  }
  .hours strong { font-weight: 600; }
</style>
</head>
<body>

<section class="poster poster--brown">
  <div class="brand-name">Hautglanz</div>
  <div class="tagline">Dein Kosmetikstudio in Göttingen</div>
  <nav class="band services">
    <span>Kosmetik</span><span>Haarentfernung</span><span>Wimpernverlängerung</span><span>Nagelstudio</span><span>Fußpflege</span>
  </nav>
  <svg class="photo photo--torn" viewBox="0 0 525 243" role="img" aria-label="Nahaufnahme eines Augenpaars hinter aufgerissenem Papier" preserveAspectRatio="none">
    <defs>
      <radialGradient id="skinTone" cx="50%" cy="55%" r="70%">
        <stop offset="0" stop-color="#e8b6a0"/>
        <stop offset="0.6" stop-color="#d49a82"/>
        <stop offset="1" stop-color="#b87a64"/>
      </radialGradient>
    </defs>
    <path fill="#e6e6e6" d="M0 22 L30 12 L60 20 L95 8 L130 18 L175 10 L210 22 L250 14 L300 20 L345 10 L390 18 L430 8 L470 16 L505 6 L525 12 L525 222 L490 232 L450 222 L410 236 L360 226 L320 238 L270 228 L225 240 L180 230 L135 238 L90 226 L45 236 L0 228 Z"/>
    <path fill="url(#skinTone)" d="M0 30 L35 20 L70 28 L100 16 L140 26 L180 18 L215 30 L255 22 L305 28 L350 18 L395 26 L435 16 L475 24 L510 14 L525 20 L525 214 L490 224 L450 214 L410 228 L360 218 L320 230 L270 220 L225 232 L180 222 L135 230 L90 218 L45 228 L0 220 Z"/>
  </svg>
  <h1 class="headline">Dauerhafte Haarentfernung</h1>
  <p class="subline">mit neueste IPL Technologie</p>
  <ul class="benefits">
    <li>Kostenlose Beratung</li>
    <li>Besonders schonend für ihre Haut</li>
    <li>Für alle Körperpartien geeignet</li>
    <li>Nie wieder rasieren, epilieren oder wachsen!</li>
  </ul>
  <div class="band contact">
    <span>Lindenweg 14, 37073 Göttingen</span><span>Tel. 0551 - 555 01 234</span><span>email@hautglanz-kosmetik.example</span>
  </div>
  <div class="hours">
    <div><strong>Öffnungszeiten</strong><br>Mo, Di, Do und Fr: 10:00 - 18:00 Uhr</div>
    <div>Mittwoch: 10:00 - 18:00 Uhr und 18:00 - 20:00 Uhr (nur mit Termin)<br>Sa (nur mit Termin): 10:00 - 14:00 Uhr</div>
  </div>
</section>

<section class="poster poster--blue">
  <div class="brand-name">Hautglanz</div>
  <div class="tagline">Dein Kosmetikstudio in Göttingen</div>
  <nav class="band services">
    <span>Kosmetik</span><span>Haarentfernung</span><span>Wimpernverlängerung</span><span>Nagelstudio</span><span>Fußpflege</span>
  </nav>
  <div class="photo photo--plain" role="img" aria-label="Nahaufnahme eines Augenpaars"></div>
  <h1 class="headline">Dauerhafte Haarentfernung</h1>
  <p class="subline">mit neueste IPL Technologie</p>
  <ul class="benefits">
    <li>Kostenlose Beratung</li>
    <li>Besonders schonend für ihre Haut</li>
    <li>Für alle Körperpartien geeignet</li>
    <li>Nie wieder rasieren, epilieren oder wachsen!</li>
  </ul>
  <div class="band contact">
    <span>Lindenweg 14, 37073 Göttingen</span><span>Tel. 0551 - 555 01 234</span><span>email@hautglanz-kosmetik.example</span>
  </div>
  <div class="hours">
    <div><strong>Öffnungszeiten</strong><br>Mo, Di, Do und Fr: 10:00 - 18:00 Uhr</div>
    <div>Mittwoch: 10:00 - 18:00 Uhr und 18:00 - 20:00 Uhr (nur mit Termin)<br>Sa (nur mit Termin): 10:00 - 14:00 Uhr</div>
  </div>
</section>

</body>
</html>
```